KESTIVA GROUP OF CLINICS

We need a medical & lab report file. The design should be healthcare related. Our current file design has been used for almost 10 years. We need something more fresh & up-to-date. We have attached the current file design.

```html
<!DOCTYPE html>
<html lang="en">
<head>
<meta charset="utf-8">
<title>Kestiva Group of Clinics – Medical Report File</title>
<link href="https://fonts.googleapis.com/css2?family=Poppins:ital,wght@0,400;0,500;0,600;0,700;1,500&display=swap" rel="stylesheet">
<style>
  :root{
    --navy:#2e3192;
    --sky:#00b4ef;
    --sky-deep:#0a9fe3;
    --cyan:#1fa9ec;
    --white:#ffffff;
    --stage:#8c8c8c;
    --photo-light:#e6ecf2;
    --photo-mid:#b9c8d8;
  }
  *{margin:0;padding:0;box-sizing:border-box;}
  html,body{width:1200px;height:699px;overflow:hidden;}
  body{background:var(--stage);font-family:"Poppins",sans-serif;color:var(--white);position:relative;}

  /* ---------- back page (branches) ---------- */
  .back-page{position:absolute;left:200px;top:79px;width:416px;height:538px;}
  .branches{position:absolute;left:0;top:0;width:416px;height:374px;
    background:linear-gradient(135deg,var(--sky) 0%,var(--sky-deep) 100%);}
  .branch{position:absolute;left:20px;width:380px;}
  .branch-tab{position:relative;display:inline-block;height:15px;padding:0 24px 0 5px;
    font-size:10px;font-weight:700;line-height:15px;letter-spacing:.1px;white-space:nowrap;}
  .branch-tab::before{content:"";position:absolute;inset:0;z-index:-1;background:var(--navy);
    clip-path:polygon(0 0,82% 0,100% 100%,0 100%);}
  .branch-tab{z-index:0;isolation:isolate;}
  .branch-info{font-size:7.9px;line-height:10.3px;margin-top:2px;white-space:nowrap;font-weight:400;}

  .contact-band{position:absolute;left:0;top:374px;width:416px;height:164px;background:var(--navy);}
  .hq-address{position:absolute;left:33px;top:33px;font-size:10.2px;line-height:11.9px;}
  .hq-lines{position:absolute;left:33px;top:85px;font-size:10px;line-height:12px;}
  .hq-line{display:flex;align-items:center;gap:6px;height:12px;}
  .hq-line svg{width:9px;height:9px;flex:none;}
  .hq-line.bold{font-weight:700;}
  .hq-web{position:absolute;left:32px;top:131px;font-size:13.5px;font-weight:700;color:var(--cyan);}
  .band-brand{position:absolute;left:247px;top:53px;transform:translateX(-50%);text-align:center;}
  .brand-dot{display:block;margin:0 auto 8px;width:30px;height:30px;border-radius:50%;background:var(--cyan);}
  .brand-name{font-size:10.5px;font-weight:600;letter-spacing:.2px;white-space:nowrap;}

  /* ---------- front cover ---------- */
  .cover{position:absolute;left:616px;top:23px;width:423px;height:648px;background:var(--navy);
    border-radius:0 16px 16px 16px;overflow:hidden;}
  .cover-brand{position:absolute;left:50%;top:88px;transform:translateX(-50%);text-align:center;}
  .cover-brand .brand-dot{background:var(--white);width:34px;height:34px;margin-bottom:12px;}
  .cover-photo{position:absolute;left:0;top:205px;width:423px;height:225px;
    background:linear-gradient(110deg,var(--photo-light) 0%,#dfe7ef 45%,var(--photo-mid) 100%);}
  .cover-title{position:absolute;left:0;right:0;top:450px;text-align:center;}
  .cover-title h1{font-size:37px;font-weight:700;line-height:40px;letter-spacing:-.3px;}
  .cover-title .tagline{font-size:16.5px;font-weight:400;line-height:20px;margin-top:1px;}
  .cover-title .privacy{font-size:11.5px;font-style:italic;font-weight:500;margin-top:6px;}
  .cover-web{position:absolute;left:0;right:0;top:614px;text-align:center;font-size:12.5px;letter-spacing:4.2px;}
</style>
</head>
<body>

<section class="back-page">
  <div class="branches">
    <div class="branch" style="top:19px">
      <div class="branch-tab">PUSAT PERUBATAN KESTIVA</div>
      <p class="branch-info">Level 18, Seri Annexe 4, No.7, Jalan Cahaya Permai, Off Jalan Cahaya Baru, 50480 Kuala Lumpur.<br>P.+603-2100 4410 F.+603-2100 4411 E.pusatkestiva@mail.com</p>
    </div>
    <div class="branch" style="top:63px">
      <div class="branch-tab">KLINIK KESTIVA (TAMAN SERI INDAH)</div>
      <p class="branch-info" style="margin-top:5px">No.22, Jalan Seri Indah 4/2, Taman Seri Indah, 40460 Shah Alam, Selangor Darul Ehsan.<br>P.+603-7720 5310 F.+603-7720 5311 E.pusatkestiva@mail.com</p>
    </div>
    <div class="branch" style="top:114px">
      <div class="branch-tab">KLINIK KESTIVA (BATU MAUNG)</div>
      <p class="branch-info" style="margin-top:5px">Lot 2A-1-1, 2A-1-2, 2A-1-3, Persiaran Merbuk, Maung Square, 11960 Batu Maung, Penang<br>P.+604-318 2040 F.+604-318 2041 E.kestivamaung@mail.com</p>
    </div>
    <div class="branch" style="top:167px">
      <div class="branch-tab">KLINIK KESTIVA (SEREMBAN JAYA)</div>
      <p class="branch-info" style="line-height:9.6px">No. 54, Jalan Niaga Seremban 2/5, Pusat Niaga Seremban Jaya<br>70450 Seremban Jaya, Negeri Sembilan.<br><span style="line-height:11px">P.+606-760 1150 F.+606-760 1151 E.kestivaseremban@mail.com</span></p>
    </div>
    <div class="branch" style="top:222px">
      <div class="branch-tab">KLINIK KESTIVA CLINIC (TERMINAL 1)</div>
      <p class="branch-info">Lot AR 12, Arrival Level, Terminal 1 Building, Airport City, 43900 Sepang, Selangor Darul Ehsan.<br>P.+603-8600 2210 F.+603-8600 2211 E.kestivaterminal1@mail.com</p>
    </div>
    <div class="branch" style="top:272px">
      <div class="branch-tab">KLINIK KESTIVA CLINIC (TERMINAL 2)</div>
      <p class="branch-info">T2-1-L08, Landside Arrival Level, Airport City, 43900 Sepang, Selangor Darul Ehsan.<br>P.+603-8600 3320 F.+603-8600 3321 E.kestivaterminal2@mail.com</p>
    </div>
    <div class="branch" style="top:315px">
      <div class="branch-tab">KLINIK KESTIVA CLINIC (NORTH TERMINAL)</div>
      <p class="branch-info" style="line-height:9.8px;margin-top:4px">Unit L1-04, Passenger Terminal Building, North Regional Airport,<br>11910 Batu Maung, Penang<br>P.+604-520 9180 F.+604-520 9181 E.kestivanorth@mail.com</p>
    </div>
  </div>

  <div class="contact-band">
    <p class="hq-address">Level 5, Block C2,<br>Cahaya Business Park (Subang)<br>Jalan Perdana U2/18 Sec<br>U2 40160 Shah Alam, Selangor</p>
    <div class="hq-lines">
      <div class="hq-line bold">
        <svg viewBox="0 0 24 24" aria-hidden="true"><path fill="#1fa9ec" d="M6.6 10.8a15.1 15.1 0 0 0 6.6 6.6l2.2-2.2a1 1 0 0 1 1-.25 11.4 11.4 0 0 0 3.6.57 1 1 0 0 1 1 1V20a1 1 0 0 1-1 1A17 17 0 0 1 3 4a1 1 0 0 1 1-1h3.5a1 1 0 0 1 1 1c0 1.25.2 2.45.57 3.57a1 1 0 0 1-.25 1z"/></svg>
        +603-5120 4400
      </div>
      <div class="hq-line bold">
        <svg viewBox="0 0 24 24" aria-hidden="true"><circle cx="12" cy="12" r="9" fill="none" stroke="#1fa9ec" stroke-width="2.4"/></svg>
        +60 12-480 6615
      </div>
      <div class="hq-line">
        <svg viewBox="0 0 24 24" aria-hidden="true"><rect x="2" y="5" width="20" height="14" rx="1.5" fill="#1fa9ec"/><path d="M3 6l9 7 9-7" fill="none" stroke="#2e3192" stroke-width="1.8"/></svg>
        hello@kestiva.my
      </div>
    </div>
    <div class="hq-web">KESTIVA.MY</div>

    <div class="band-brand">
      <span class="brand-dot"></span>
      <div class="brand-name">KESTIVA GROUP</div>
    </div>
  </div>
</section>

<section class="cover">
  <div class="cover-brand">
    <span class="brand-dot"></span>
    <div class="brand-name">KESTIVA GROUP</div>
  </div>
  <div class="cover-photo" role="img" aria-label="Photograph of a patient lying on a scanner table in a bright medical imaging room"></div>
  <div class="cover-title">
    <h1>MEDICAL REPORT</h1>
    <p class="tagline">YOUR HEALTHCARE PARTNER!</p>
    <p class="privacy">Private &amp; Confidential</p>
  </div>
  <div class="cover-web">WWW.KESTIVA.MY</div>
</section>

</body>
</html>
```